Tombo's Pan. Chicken shop

yDesign special menu with special pictures within 48 h
Very smaple menu

Target Market(s)

Local

Industry/Entity Type

Food

Colors
FFF300
FFF600
FEFA6F
FFFEC7
FFFEE8

Requirements
Must have
• IGood quality picture
Nice to have
• Good quality pictures

```html
<!DOCTYPE html>
<html lang="en">
<head>
<meta charset="utf-8">
<title>Tombo's Pan – Menu</title>
<link href="https://fonts.googleapis.com/css2?family=Archivo+Black&family=Montserrat:wght@700&family=Questrial&display=swap" rel="stylesheet">
<style>
:root{
  --yellow:#FFF300;
  --yellow-alt:#FFF600;
  --yellow-soft:#FEFA6F;
  --cream:#FFFEC7;
  --ink:#000;
  --white:#fff;
}
*{margin:0;padding:0;box-sizing:border-box}
html,body{width:1200px;height:848px;overflow:hidden;background:#ecebe4}
body{font-family:"Questrial",sans-serif;font-size:13px;line-height:17px;color:var(--ink)}
.menu{position:relative;width:1200px;height:848px}
.abs{position:absolute}

/* ---------- left page ---------- */
.page-left{position:absolute;left:0;top:0;width:656px;height:848px;overflow:hidden;
  background:repeating-linear-gradient(90deg,var(--yellow) 0 11px,var(--yellow-alt) 11px 22px)}
.page-left::after{content:"";position:absolute;left:0;right:0;top:827px;height:5px;background:var(--ink)}
.brand{left:0;width:656px;top:30px;text-align:center;font-family:"Archivo Black",sans-serif;font-size:50px;line-height:60px;color:var(--ink)}
.heading{font-family:"Archivo Black",sans-serif;font-weight:400;font-size:20px;line-height:24px;letter-spacing:.3px;white-space:nowrap}
.subhead{font-family:"Archivo Black",sans-serif;font-size:16px;line-height:20px;white-space:nowrap}
.step-title{font-family:"Archivo Black",sans-serif;font-size:16px;line-height:20px;white-space:nowrap}
.col-rule{position:absolute;width:0;border-left:1px solid rgba(0,0,0,.4)}
.price-row{display:flex;width:122px;white-space:nowrap}
.price-row i{flex:1;border-bottom:1px dotted var(--ink);margin:0 1px 4px}
.sauce-band{left:0;top:304px;width:473px;height:41px;background:var(--ink);padding:2px 30px;color:var(--yellow)}
.sauce-band p{white-space:nowrap}
.sandwich-list{left:30px;top:542px;width:614px}
.item-name{font-family:"Archivo Black",sans-serif;font-size:16px;line-height:20px;white-space:nowrap}
.item-name small{font-family:"Questrial",sans-serif;font-size:13px}
.item-desc{line-height:17.5px;white-space:nowrap}
.leader{display:flex;white-space:nowrap}
.leader i{flex:1;border-bottom:1px dotted var(--ink);margin:0 1px 4px;min-width:4px}
.leader b{font-weight:700}
.photo{position:absolute;border-radius:40%}

/* ---------- right page ---------- */
.page-right{position:absolute;left:656px;top:0;width:544px;height:848px;overflow:hidden;
  background:linear-gradient(160deg,#050505 0%,#1e1b1a 40%,#33281f 70%,#161311 100%);color:var(--white)}
.page-right::after{content:"";position:absolute;left:0;right:0;top:826px;height:5px;background:var(--yellow)}
.scene{left:40px;top:300px;width:440px;height:520px;border-radius:50%;
  background:radial-gradient(ellipse at 50% 50%,rgba(140,55,40,.5),rgba(60,40,30,0) 70%)}
.r-block{left:19px;width:510px;white-space:nowrap}
.r-title{font-family:"Montserrat",sans-serif;font-weight:700;font-size:16px;line-height:20px;color:var(--yellow)}
.r-title span{font-family:"Questrial",sans-serif;font-weight:400;font-size:13px;color:var(--white)}
.r-step{font-family:"Montserrat",sans-serif;font-weight:700;font-size:15px;line-height:20px;color:var(--yellow)}
.r-step em,.r-price{font-family:"Questrial",sans-serif;font-style:normal;font-weight:400;font-size:13px;color:var(--yellow)}
.dots{display:inline-block;border-bottom:1px dotted var(--yellow);vertical-align:3px}
.r-sub{font-family:"Montserrat",sans-serif;font-weight:700;font-size:13px;color:var(--yellow)}
.divider{position:absolute;left:19px;width:499px;border-top:1px dotted rgba(255,243,0,.55)}
</style>
</head>
<body>
<div class="menu">

  <section class="page-left">
    <div class="abs brand">TOMBO'S PAN</div>

    <div class="photo" role="img" aria-label="Photo of crispy breaded chicken wings" style="left:496px;top:106px;width:110px;height:112px;background:radial-gradient(circle at 45% 45%,#e8902c,#b75414 65%,rgba(183,84,20,0) 72%)"></div>
    <div class="photo" role="img" aria-label="Photo of flame grilled chicken skewers" style="left:485px;top:255px;width:150px;height:133px;background:radial-gradient(circle at 50% 50%,#c8401c,#7a2410 60%,rgba(122,36,16,0) 72%)"></div>
    <div class="photo" role="img" aria-label="Photo of a double cheeseburger" style="left:506px;top:434px;width:146px;height:150px;background:radial-gradient(circle at 50% 50%,#c98a3a,#6b3a1a 60%,rgba(107,58,26,0) 72%)"></div>

    <h2 class="abs heading" style="left:30px;top:116px">BREADED WINGS</h2>
    <p class="abs subhead" style="left:30px;top:141px">ALL WINGS SERVED WITH FRIES &amp; 1 dip</p>

    <p class="abs step-title" style="left:30px;top:166px">Step 1.<br>Wings<br>Boneless</p>
    <span class="col-rule" style="left:128px;top:170px;height:124px"></span>
    <div class="abs" style="left:144px;top:166px">
      <p class="step-title">Step 2</p>
      <p class="price-row"><span>4 wings</span><i></i><span>6.99</span></p>
      <p class="price-row"><span>8 Wings</span><i></i><span>9.75£</span></p>
      <p class="price-row"><span>10 wings</span><i></i><span>11.50</span></p>
      <p class="price-row"><span>12 Wings</span><i></i><span>12.95</span></p>
    </div>
    <span class="col-rule" style="left:282px;top:170px;height:124px"></span>
    <div class="abs" style="left:297px;top:166px">
      <p class="step-title">Step 3</p>
      <p class="step-title">Choose your&nbsp; flavour</p>
      <p>1 Original | 2 buffalo<br>3 bbq | 4 lemon paper<br>5 garlic parmesan<br>6 dynamite |7 Nashville oh<br>hot damn</p>
    </div>

    <div class="abs sauce-band">
      <p class="step-title">Step 4 Choose your sause</p>
      <p>Blue cheese | Honey mustard | House ranch | Tombo's special</p>
    </div>

    <h2 class="abs heading" style="left:30px;top:519px;top:519px;top:518px;top:518px;top:520px;top:519px;top:518px;top:519px;top:519px;top:519px;top:519px;top:519px;top:519px;top:519px;top:519px;top:519px;top:519px;top:519px;top:519px;top:354px">BUTTERMILK MARINATED TENDERS</h2>
    <p class="abs heading" style="left:30px;top:380px;font-size:19px">ALL Tenders SERVED WITH FRIES &amp; 1 dip</p>

    <div class="abs" style="left:30px;top:409px">
      <p class="step-title">Step 1.</p>
      <p>Large | Mini</p>
      <p class="step-title" style="margin-top:14px">Step 2</p>
      <p>3&nbsp; tenders &nbsp;&nbsp;&nbsp;&nbsp;&nbsp;5.99£</p>
      <p>6 tenders&nbsp; 8.99</p>
    </div>
    <span class="col-rule" style="left:166px;top:413px;height:124px"></span>
    <div class="abs" style="left:178px;top:409px">
      <p class="step-title">Step 3</p>
      <p>Choose your falvour<br>1 Original, 2 buffalo<br>3 bbq, 4 lemon paper<br>5 garlic parmesan<br>6 dynamite ,7 Nashville<br>oh hot damn</p>
    </div>
    <span class="col-rule" style="left:338px;top:413px;height:124px"></span>
    <div class="abs" style="left:349px;top:409px">
      <p class="step-title">Step 4</p>
      <p class="step-title">Choose your sause</p>
      <p>Blue cheese<br>Honey mustard<br>House ranch<br>Tombo's special</p>
    </div>

    <div class="abs sandwich-list">
      <p class="item-name">Sandwich&nbsp; option 1</p>
      <p class="item-desc">All meals servived with chips and dip</p>
      <p class="item-name">1-Classic burger</p>
      <p class="item-desc leader"><span>Fried chicken breast, fresh pickles &amp; creamy mayo in a soft brioche bun</span><i></i><b>5.50</b></p>
      <p class="item-name">2-Tombo's special</p>
      <p class="item-desc leader"><span>(Relish sauce, Fried chicken breast,Honey mustard, Red cabbage in a soft brioche bun )</span><i></i><b>6.95</b></p>
      <p class="item-name">3- Nashville oh hot damn</p>
      <p class="item-desc leader"><span>Fried nashville chicken breast, fresh pickles &amp; Tombo's sause, pot of grave&amp; mash potato</span><i></i><b>7.99</b></p>
      <p class="item-name">5-double cheesy toasted</p>
      <p class="item-desc leader"><span>( tenders ,Cheese, slaw, pickles, mayo)</span><i></i><b>5.99</b></p>
      <p class="item-name leader"><span>6 Dynamite Burger</span><i></i><b style="font-family:'Questrial',sans-serif;font-size:13px">6.50</b></p>
      <p class="item-desc">Sweet mayo, Iceberg lettuce, Fried chicken breast,Dynamite sauce , soft deli rolls</p>
      <p class="item-name">7-Mini fillet Slider<small>(lemon herbs ,Demled peri peri ,mangolime)</small></p>
      <p class="item-desc leader"><span>( Mini Fillet ,lettus ,Cheese ,Select your flavoursin a mini bun)</span><i></i><b>4.99</b></p>
    </div>
  </section>

  <section class="page-right">
    <div class="abs scene" role="img" aria-label="Dark food photo of a sub roll, tomato slices and salami"></div>
    <div class="photo" role="img" aria-label="Photo of a loaded chicken sub sandwich" style="left:384px;top:155px;width:130px;height:76px;background:radial-gradient(ellipse at 50% 50%,#d9a25a,#8a5a2a 60%,rgba(138,90,42,0) 72%)"></div>
    <div class="photo" role="img" aria-label="Photo of cheesy loaded fries" style="left:392px;top:370px;width:126px;height:70px;background:radial-gradient(ellipse at 50% 50%,#f2b43a,#b07420 60%,rgba(176,116,32,0) 72%)"></div>
    <div class="photo" role="img" aria-label="Photo of saucy chicken wings with a dip bowl" style="left:410px;top:531px;width:124px;height:100px;background:radial-gradient(ellipse at 50% 50%,#c5501e,#7a2a10 60%,rgba(122,42,16,0) 72%)"></div>

    <div class="abs r-block" style="top:34px">
      <p class="r-title">SANDWICH&nbsp; <span>All meals servied with chips and dip&nbsp; option 2</span></p>
      <p class="r-step">Step 1</p>
      <p>Select your base<span class="dots" style="width:72px"></span><span class="r-price">2.50</span></p>
      <p>Brioche bun , soft deli roll , Waffle, double Chesney toasted</p>
      <p class="r-step">Step 2</p>
      <p>Select your chicken<span class="dots" style="width:52px"></span><span class="r-price">3.50</span></p>
      <p>Tenders , chicken breasrt</p>
      <p class="r-step">Step 3<span class="dots" style="width:124px"></span><em>2.50</em></p>
      <p>Select your favourite sause</p>
      <p>Classic ,Buffalo, Bbq, Mango lime, Daynmat</p>
      <p>Lemon herbs, Nashville, Demless peri peri</p>
      <p class="r-step">Step 4</p>
      <p>Add topping | Cheese | Lettuce| Slaw | Pickles</p>
      <p class="r-step">Step 5<span class="dots" style="width:124px"></span><em>0.00</em></p>
      <p>Select your sause</p>
      <p>Blue cheese | Honey mustard&nbsp; | House ranch&nbsp; | Daynmaited</p>
      <p>Tombo's special</p>
    </div>

    <span class="divider" style="top:360px"></span>

    <div class="abs r-block" style="top:377px;left:22px">
      <p class="r-title">Sides</p>
      <p>1 chicken pop corn<span class="dots" style="width:52px"></span><span class="r-price">5.50</span></p>
      <p>Chicken pop corn topped with meltd cheddar cheese,</p>
      <p>dynamite sasue , sismes</p>
      <p>2 chilli cheese bites | Chilli cheese bites , Select your dip</p>
      <p>3 mozerla stick | 4 halomi stick | 5 garlic mushrooms bites</p>
      <p>6 onion rings</p>
      <p>Mac &amp; cheese bites | Tombo's special ( mash potato,&nbsp; grave sause )</p>
      <p>Honey mustard slaw</p>
    </div>

    <span class="divider" style="top:548px"></span>

    <div class="abs r-block" style="top:557px;left:20px">
      <p class="r-title">Loaded FRIES</p>
      <p class="r-title">Fry by</p>
      <p>Chips loaded with melted cheese , daynmite sause , jalapeño</p>
      <p class="r-sub">Takes loaded</p>
      <p>Chips load3d with melted cheese,&nbsp; hot sause , takes</p>
      <p class="r-sub">Chicketoos</p>
      <p>Chips tenders loaded with nelt3d cheese , ketchup,&nbsp; crunchos</p>
      <p class="r-sub">Oh hot damn</p>
      <p>Chips nashville tender , melted cheese , sarcha sause , green chilli paper</p>
      <p class="r-sub">Pop corn</p>
      <p>Chips Chicken pop corn , melted cheese , Daynmaited sause , Sesame</p>
      <p>Chips , tenders , montero jack cheese, crispy Fried onion , Tombo's dressing</p>
      <p class="r-sub">Seasoned FRIES | Regular FRIES | Regular Sweet potato | Cajuan FRIES</p>
      <p class="r-sub">Haloomi FRIES</p>
    </div>
  </section>

</div>
</body>
</html>
```